FULL Page Ad - Modern Elegant

- I need a 8.5" x 11" trim ad with 0.25" bleed. Live information should be at least 0.5" from edges.

Target Market(s)

Insurance Company Decision Makers

Industry/Entity Type

Insurance

Colors

Designer to choose colors to be used in the design.

Requirements
Nice to have
• Would like colors matched to our logo. Would like incorporation of natural disasters (tornado, hail, hurricane or things like house fires)

```html
<!DOCTYPE html>
<html lang="en">
<head>
<meta charset="utf-8">
<title>24/7 Emergency Response Center – Full Page Ad</title>
<link rel="stylesheet" href="https://fonts.googleapis.com/css2?family=Roboto:wght@400;500;700;900&display=swap">
<style>
  :root {
    --stage: #ffffff;
    --purple: #382d87;
    --purple-deep: #2f2870;
    --purple-band: #2c2468;
    --orange: #f0781d;
    --white: #ffffff;
  }
  html, body {
    margin: 0;
    width: 1200px;
    height: 1200px;
    overflow: hidden;
    background: var(--stage);
  }
  .ad-page {
    position: absolute;
    left: 294px;
    top: 204px;
    width: 612px;
    height: 792px;
    display: block;
  }
  .ad-page text { font-family: "Roboto", Arial, sans-serif; }
  .brand-name { fill: var(--orange); font-weight: 700; font-size: 22px; letter-spacing: 1px; }
  .headline-hours { fill: var(--white); font-weight: 700; font-size: 118px; }
  .headline-title { fill: var(--orange); font-weight: 700; font-size: 94px; }
  .hotline { fill: var(--white); font-weight: 700; font-size: 58px; }
  .contact-line { fill: var(--orange); font-weight: 400; font-size: 29px; }
  .rule { stroke: var(--white); stroke-width: 4; }
  .icon-shape { fill: var(--orange); }
</style>
</head>
<body>
<svg class="ad-page" viewBox="0 0 985 1275" xmlns="http://www.w3.org/2000/svg">
  <defs>
    <linearGradient id="fire-tones" x1="0" y1="0" x2="0" y2="1">
      <stop offset="0" stop-color="#3b3636"/>
      <stop offset="0.45" stop-color="#c2521d"/>
      <stop offset="1" stop-color="#4e5a3a"/>
    </linearGradient>
    <linearGradient id="tornado-tones" x1="0" y1="0" x2="0" y2="1">
      <stop offset="0" stop-color="#4d5a55"/>
      <stop offset="0.6" stop-color="#c9cdc6"/>
      <stop offset="0.78" stop-color="#e3e5df"/>
      <stop offset="0.85" stop-color="#2b3528"/>
      <stop offset="1" stop-color="#1e261c"/>
    </linearGradient>
    <linearGradient id="hurricane-tones" x1="0" y1="0" x2="0" y2="1">
      <stop offset="0" stop-color="#d9dcd9"/>
      <stop offset="0.45" stop-color="#5f6f4e"/>
      <stop offset="0.7" stop-color="#c8b77a"/>
      <stop offset="1" stop-color="#8a8274"/>
    </linearGradient>
  </defs>

  <!-- base -->
  <rect class="page-base" width="985" height="1275" fill="var(--purple)"/>
  <polygon class="page-shade" points="0,0 192,0 470,370 0,732" fill="var(--purple-deep)"/>

  <!-- diagonal bands -->
  <polygon class="band" points="852,0 947,0 487,382 440,330" fill="var(--purple-band)"/>
  <polygon class="band" points="985,572 985,640 809,782 767,737" fill="var(--purple-band)"/>
  <polygon class="band" points="767,737 809,782 767,817 730,780" fill="var(--purple-band)"/>

  <!-- imagery panels -->
  <polygon role="img" aria-label="Photo: house on fire with firefighters on the lawn"
           points="192,0 852,0 440,330" fill="url(#fire-tones)"/>
  <polygon role="img" aria-label="Photo: tornado touching down over a flat field"
           points="947,0 985,0 985,572 767,737 487,382" fill="url(#tornado-tones)"/>
  <polygon role="img" aria-label="Photo: hurricane winds bending palm trees over a flooded street"
           points="767,817 985,1092 985,1275 262,1275" fill="url(#hurricane-tones)"/>
  <polygon class="accent-triangle" points="809,782 985,637 985,1002" fill="var(--orange)"/>

  <!-- brand -->
  <text class="brand-name" x="62" y="108">VANTAGE ADJUSTERS</text>

  <!-- headline -->
  <text class="headline-hours" x="58" y="402">24/7</text>
  <line class="rule" x1="62" y1="424" x2="335" y2="424"/>
  <text class="headline-title" x="58" y="517">EMERGENCY</text>
  <text class="headline-title" x="58" y="622">RESPONSE</text>
  <text class="headline-title" x="58" y="727">CENTER</text>
  <line class="rule" x1="62" y1="759" x2="628" y2="759"/>

  <!-- hotline -->
  <g class="hotline-icon" transform="translate(62,790)">
    <path d="M8 4 L18 4 L22 16 L15 21 Q22 36 36 42 L41 35 L53 39 L53 50 Q50 56 42 55 Q10 48 2 14 Q2 5 8 4 Z"
          fill="none" stroke="var(--orange)" stroke-width="5" stroke-linejoin="round"/>
    <circle cx="35" cy="22" r="3" fill="var(--orange)"/>
    <circle cx="45" cy="22" r="3" fill="var(--orange)"/>
    <circle cx="55" cy="22" r="3" fill="var(--orange)"/>
  </g>
  <text class="hotline" x="148" y="837">(800) 555-0142</text>

  <!-- contact details -->
  <g class="contact-icon icon-pin" transform="translate(84,1019)">
    <path class="icon-shape" d="M0 -14 a10 10 0 0 1 10 10 c0 8 -10 18 -10 18 c0 0 -10 -10 -10 -18 a10 10 0 0 1 10 -10 z"/>
    <circle cx="0" cy="-4" r="3.5" fill="var(--purple)"/>
  </g>
  <text class="contact-line" x="123" y="1029">214 Mill Street</text>
  <text class="contact-line" x="123" y="1064">PO Box 318</text>
  <text class="contact-line" x="123" y="1099">Harlow Falls, NY 12099</text>

  <g class="contact-icon icon-phone" transform="translate(84,1139)">
    <path class="icon-shape" d="M-12 -11 L-5 -11 L-2 -3 L-6 0 Q-2 7 5 10 L8 6 L14 8 L14 14 Q12 17 7 16 Q-10 11 -14 -6 Q-14 -10 -12 -11 Z"/>
  </g>
  <text class="contact-line" x="123" y="1149">(800) 555-0187</text>

  <g class="contact-icon icon-mail" transform="translate(84,1192)">
    <rect x="-14" y="-10" width="28" height="20" rx="2" class="icon-shape"/>
    <path d="M-14 -8 L0 3 L14 -8" fill="none" stroke="var(--purple)" stroke-width="2"/>
  </g>
  <text class="contact-line" x="123" y="1202">claims@vantageadjusters.com</text>
</svg>
</body>
</html>
```